CareVantRx business cards

We need a business card design that we could customize as needed for employees. We will need space for Name, Title, 1-2 phone numbers and email address.

We are a Pharmacy Benefits Management (PBM) company for hospice agencies and beginning a nationwide expansion. Attached is a vector file of our logo.

Cards can be single or double sided.

Industry/Entity Type

Business

```html
<!DOCTYPE html>
<html lang="en">
<head>
<meta charset="UTF-8">
<title>CareVantRx Business Cards</title>
<link rel="stylesheet" href="https://fonts.googleapis.com/css2?family=Open+Sans:wght@400;600&family=Questrial&display=swap">
<style>
  :root {
    --page: #e9e6e1;
    --card-white: #ffffff;
    --card-black: #000000;
    --brand-blue: #2f6a93;
    --brand-green: #8a9d45;
    --name-orange: #d4572a;
    --ink: #222222;
    --icon-grey: #7a8a55;
    --band-text: #ffffff;
  }
  * { box-sizing: border-box; margin: 0; padding: 0; }
  html, body {
    width: 1200px; height: 1186px; overflow: hidden;
    background: var(--page);
    font-family: "Open Sans", Arial, sans-serif;
  }
  .canvas { position: relative; width: 1200px; height: 1186px; }

  .card {
    position: absolute; width: 881px; height: 502px; overflow: hidden;
    box-shadow: 0 2px 6px rgba(0,0,0,0.25);
  }
  .card--front { left: 263px; top: 49px; background: var(--card-white); border: 1px solid #555; }
  .card--back { left: 43px; top: 619px; background: var(--card-black); }

  .brand { position: absolute; display: flex; align-items: center; gap: 22px; }
  .brand__square { width: 93px; height: 93px; border-radius: 12px; background: var(--brand-blue); flex: none; }
  .brand__name {
    font-family: "Questrial", "Open Sans", sans-serif;
    font-size: 86px; line-height: 1; color: var(--brand-blue); letter-spacing: -1px;
  }
  .card--front .brand { left: 52px; top: 32px; }
  .card--back .brand { left: 131px; top: 189px; }
  .card--back .brand__square { width: 100px; height: 100px; }

  .person { position: absolute; left: 52px; top: 205px; font-size: 24px; color: var(--ink); }
  .person__name { color: var(--name-orange); font-size: 31px; font-weight: 600; }

  .contact { position: absolute; left: 52px; top: 267px; list-style: none; }
  .contact__item {
    display: flex; align-items: center; gap: 9px;
    height: 34px; font-size: 21px; color: var(--ink);
  }
  .contact__item svg { width: 17px; height: 17px; fill: var(--icon-grey); flex: none; }

  .rule { position: absolute; left: 0; right: 0; top: 438px; height: 3px; background: var(--brand-blue); }
  .address-band {
    position: absolute; left: 0; right: 0; top: 446px; height: 56px;
    background: var(--brand-green); color: var(--band-text);
    font-size: 19px; font-weight: 600; padding-left: 52px; line-height: 56px;
  }
  .corner-tab {
    position: absolute; left: 669px; top: 430px; width: 134px; height: 38px;
    background: var(--card-white); border-radius: 0 0 16px 16px;
  }
  .corner-square {
    position: absolute; left: 687px; top: 356px; width: 97px; height: 97px;
    border-radius: 12px; background: var(--brand-blue);
  }

  .web-address {
    position: absolute; left: 0; right: 0; top: 382px; text-align: center;
    color: #ffffff; font-size: 30px; letter-spacing: 3px;
  }
</style>
</head>
<body>
<main class="canvas">

  <section class="card card--front" aria-label="Business card front">
    <div class="brand">
      <span class="brand__square"></span>
      <span class="brand__name">CareVantRx</span>
    </div>

    <p class="person"><span class="person__name">Your Name,</span> Title</p>

    <ul class="contact">
      <li class="contact__item">
        <svg viewBox="0 0 16 16" aria-hidden="true"><path d="M3.5 1.5l2.5 0 1 3.5-1.7 1.2c.8 1.8 2.2 3.2 4 4l1.2-1.7 3.5 1v2.5c0 1-1 2-2 2C6.5 14 2 9.5 1.5 3.5c0-1 1-2 2-2z"/></svg>
        012-345-6789
      </li>
      <li class="contact__item">
        <svg viewBox="0 0 16 16" aria-hidden="true"><rect x="4" y="1" width="8" height="14" rx="1.5"/><rect x="5.5" y="3" width="5" height="8" fill="#fff"/></svg>
        012-345-6789
      </li>
      <li class="contact__item">
        <svg viewBox="0 0 16 16" aria-hidden="true"><path d="M1 4h14v9H1z"/><path d="M1 4l7 5 7-5" fill="none" stroke="#fff" stroke-width="1.4"/></svg>
        info@carevantrx.com
      </li>
      <li class="contact__item">
        <svg viewBox="0 0 16 16" aria-hidden="true"><circle cx="8" cy="8" r="7"/><path d="M1 8h14M8 1c-3 3-3 11 0 14M8 1c3 3 3 11 0 14" fill="none" stroke="#fff" stroke-width="1"/></svg>
        www.carevantrx.com
      </li>
    </ul>

    <div class="rule"></div>
    <div class="address-band">Sreet Name, City Name, Zip Code-00000</div>
    <div class="corner-tab"></div>
    <span class="corner-square"></span>
  </section>

  <section class="card card--back" aria-label="Business card back">
    <div class="brand">
      <span class="brand__square"></span>
      <span class="brand__name">CareVantRx</span>
    </div>
    <p class="web-address">www.carevantrx.com</p>
  </section>

</main>
</body>
</html>
```